Brand refresh of quote, work docket and Fire certificate documents

I would like a refresh of our document suit including

1. Front page called VOLT3 Proposal
2. Quote document template
3. Work docket template
4. Fire certificate template - to look like a professional complaint certificate

Examples of documents are attached.

```html
<!DOCTYPE html>
<html lang="en">
<head>
<meta charset="utf-8">
<title>VOLT3 Document Suite</title>
<link rel="stylesheet" href="https://fonts.googleapis.com/css2?family=Lexend:wght@300;400;600;700&family=Poppins:wght@600;700;800&display=swap">
<style>
:root{
  --stage:#6e7170;
  --ink:#3a393e;
  --dark:#3b3a40;
  --orange:#e9532b;
  --orange-light:#f2805c;
  --page-top:#f1f1f1;
  --page-mid:#d6d6d6;
  --white:#ffffff;
}
*{margin:0;padding:0;box-sizing:border-box}
html,body{width:1200px;height:530px;overflow:hidden;background:var(--stage)}
body{position:relative;font-family:"Lexend",sans-serif;color:var(--ink)}
.page{position:absolute;top:21px;width:375px;height:485px;overflow:hidden;
  background:linear-gradient(180deg,var(--page-top) 0%,#e3e3e3 30%,var(--page-mid) 70%,#e6e6e6 100%);
  box-shadow:2px 3px 6px rgba(0,0,0,.35)}
.page--docket{left:22px}
.page--quote{left:409px}
.page--cert{left:796px}
.abs{position:absolute}
.header-swoosh{position:absolute;left:0;top:0}
.company-address{position:absolute;right:143px;top:20px;text-align:right;font-size:4.3px;line-height:6.4px;font-weight:300}
.company-address b{font-weight:600}
.brand-divider{position:absolute;left:242px;top:11px;width:.6px;height:51px;background:var(--dark)}
.brand-name{position:absolute;left:254px;top:30px;font-family:"Lexend",sans-serif;font-weight:600;font-size:18px;line-height:1;color:var(--dark)}
.brand-mark{position:absolute;left:325px;top:35px;width:8px;height:8px;background:var(--orange)}
.date-tab{position:absolute;left:0;height:7px;width:105px;border-radius:0 4px 4px 0;
  background:linear-gradient(90deg,var(--orange),var(--orange-light) 70%,#f6a88c);
  color:var(--white);font-family:"Poppins",sans-serif;font-weight:700;font-size:5.3px;line-height:7px;padding-left:42px}
.title-bar{position:absolute;left:0;height:19px;border-radius:0 10px 0 0;
  background:linear-gradient(90deg,var(--orange) 0%,#e45f37 22%,#4a4044 55%,var(--dark) 100%);
  color:var(--white);font-family:"Poppins",sans-serif;font-weight:700;font-size:11.5px;line-height:19px;padding-left:43px}
.doc-number{position:absolute;right:36px;font-family:"Lexend",sans-serif;font-weight:600;font-size:6.6px;padding-bottom:1px;border-bottom:.8px solid var(--orange)}
.body-text{font-size:4.7px;line-height:6.6px;font-weight:300}
.body-text b,.strong{font-weight:600}
.section-bar{position:absolute;height:8px;border-radius:0 6px 0 0;
  background:linear-gradient(90deg,var(--orange) 0%,#dd5a33 22%,#4b4145 55%,var(--dark) 100%);
  color:var(--white);font-weight:600;font-size:5.6px;line-height:8px;padding-left:3px}
.works-box{position:absolute;left:40px;width:296px;background:var(--white)}
.works-divider{position:absolute;width:.8px;background:var(--dark)}
.item{position:absolute;width:138px;font-size:4.7px;line-height:6.4px;font-weight:300}
.item h4{font-size:4.9px;font-weight:600;line-height:7.4px}
.item .tag{font-weight:600}
.row{position:absolute;font-size:4.8px;line-height:7.8px;font-weight:300}
.price{font-weight:600}
.total-bar{position:absolute;left:0;width:375px;background:linear-gradient(90deg,var(--orange) 0%,#d9573a 20%,#4a4145 50%,var(--dark) 100%);
  color:var(--white);font-size:6.6px;padding-left:43px}
.total-bar b{font-weight:700}
.notice-bar{position:absolute;left:0;width:375px;height:9px;background:linear-gradient(180deg,#8f8f92,#6c6c70);
  color:var(--white);font-size:4.8px;font-weight:600;line-height:9px;text-align:center}
.accept-area{position:absolute;left:0;top:407px;width:375px;height:78px;background:var(--white)}
.sign-line{display:inline-block;border-bottom:.5px solid var(--ink);height:4px;vertical-align:baseline}
.signature{position:absolute;background:linear-gradient(135deg,#ededed,#d9d9d9);border-radius:2px}
.cert-title{position:absolute;left:0;width:170px;height:26px;border-radius:0 12px 0 0;
  background:linear-gradient(90deg,var(--orange) 0%,#e45f37 22%,#4a4044 55%,var(--dark) 100%);
  color:var(--white);font-family:"Poppins",sans-serif;font-weight:700;font-size:10px;line-height:9.4px;padding:3.5px 0 0 43px}
</style>
</head>
<body>

<section class="page page--docket" aria-label="Work docket">
  <svg class="header-swoosh" width="375" height="72" viewBox="0 0 375 72">
    <path d="M150 0 C178 0 186 22 196 42 C208 64 226 68 258 68 H375 V0 Z" fill="#fff"/>
    <path d="M150 0 C178 0 186 22 196 42 C208 64 226 68 258 68 H375" fill="none" stroke="#e9532b" stroke-width=".8"/>
  </svg>
  <div class="company-address"><b>VOLT3 Pty Ltd</b><br>9/40 Ironbark Way<br>Brookvale VIC 3180<br>ABN: 48 602 115 309<br>office@volt3.com.au</div>
  <div class="brand-divider"></div>
  <div class="brand-name">VOLT3</div>
  <div class="brand-mark"></div>
  <div class="date-tab" style="top:20px">26th October, 2023</div>
  <div class="title-bar" style="top:28px;width:156px">WORK DOCKET</div>

  <div class="abs body-text" style="left:43px;top:53px"><b>Harbourline Builders</b><br>48 Wattle Row<br>Westbay VIC 3207<br>Marco</div>
  <div class="doc-number" style="top:68px">Work Docket: 1188</div>
  <div class="abs body-text" style="left:43px;top:91px">Works completed at 9 Lindell Street, Ashvale as directed by Marco of Harbourline Builders as listed below.</div>

  <div class="section-bar" style="left:40px;top:106px;width:318px">Works Completed:</div>
  <div class="works-box" style="top:114px;height:201px"></div>
  <div class="works-divider" style="left:186px;top:114px;height:201px"></div>

  <div class="item" style="left:43px;top:118px"><h4>Basement 1 – Fan Room</h4>1 x 20mm x 20mm penetration with conduit through blockwork wall (?)</div>
  <div class="item" style="left:43px;top:148px"><h4>Basement 1 – Apartment 38 Garage</h4>2 x 100mm x 100mm penetration with sprinkler pipe &amp; wrap through slab wall<br><span class="tag">(Wet Fire)</span></div>
  <div class="item" style="left:43px;top:186px"><h4>Basement 1 – Apartment 34 Garage</h4>2 x 100mm x 100mm penetration with sprinkler pipe &amp; wrap through slab wall<br><span class="tag">(Wet Fire)</span></div>
  <div class="item" style="left:43px;top:224px"><h4>Basement 1 – Apartment 30 Garage</h4>2 x 100mm x 100mm penetration with sprinkler pipe &amp; wrap through slab wall<br><span class="tag">(Wet Fire)</span></div>
  <div class="item" style="left:43px;top:262px"><h4>Basement 1 – Apartment 28</h4>5mtrs of caulking through slab wall (one side only)<br><span class="tag">(Brickies)</span></div>
  <div class="item" style="left:43px;top:292px"><h4>Basement 1 – Apartment 28</h4>5mtrs of caulking through slab wall (one side only)<br><span class="tag">(Brickies)</span></div>

  <div class="item" style="left:192px;top:118px"><h4>Basement 1 – Back Stairwell</h4>1 x 400mm x 400mm penetration empty through blockwork wall<br><span class="tag">(Builder)</span></div>
  <div class="item" style="left:192px;top:156px"><h4>Basement 1 – Apartment Bin Room</h4>1 x 80mm x 80mm penetration with sprinkler pipe &amp; wrap through blockwork wall<br><span class="tag">(Wet Fire)</span><br>2 x 20mm x 20mm penetration with conduit through blockwork wall (?)<br>2 x 20mm x 20mm penetration with conduit through blockwork wall (?)</div>
  <div class="item" style="left:192px;top:223px"><h4>Basement 1 – Comms Room</h4>2 x 300mm x 300mm penetration empty through slab wall<br><span class="tag">(Builder)</span></div>
  <div class="item" style="left:192px;top:255px"><h4>Basement 1 – Switchboard Room</h4>1 x 400mm x 100mm penetration empty through blockwork wall<br><span class="tag">(Builder)</span><br>12mtrs of caulking through blockwork wall (one side only)<br><span class="tag">(Brickies)</span></div>

  <div class="section-bar" style="left:40px;top:320px;width:318px">Labour</div>
  <div class="row" style="left:43px;top:331px">21/10/23</div>
  <div class="row" style="left:131px;top:331px">2 Men x 5hrs = 10hrs<br>(time &amp; a half rate)</div>
  <div class="row price" style="left:241px;top:331px">$1500.00</div>

  <div class="section-bar" style="left:40px;top:352px;width:318px">Materials</div>
  <div class="row" style="left:43px;top:363px">1 x Fire Mortar (20kg bag)<br>2 x Rod (Bundle)<br>15 x Caulk (Ltr)<br>4 x Sealant 300ml<br>1 x Pipe Wrap 40 (Roll)<br>¾ x Cable Wrap (Roll)</div>
  <div class="row price" style="left:241px;top:363px">$150.00<br>$100.00<br>$375.00<br>$120.00<br>$220.00<br>$450.00</div>

  <div class="section-bar" style="left:40px;top:415px;width:318px">Breakdown:</div>
  <div class="row" style="left:43px;top:425px">Conduits (unknown) 10% - 291.50 + GST<br>Wet Fire 45% - $1,311 + GST<br>Brickies 20% - $583 + GST<br>Builder 25% - $728.75 + GST</div>

  <div class="total-bar" style="top:463px;height:13px;line-height:13px">Price for Labour &amp; Materials - <b>TOTAL: $2,915 + GST</b></div>
</section>

<section class="page page--quote" aria-label="Quote">
  <svg class="header-swoosh" width="375" height="72" viewBox="0 0 375 72">
    <path d="M150 0 C178 0 186 22 196 42 C208 64 226 68 258 68 H375 V0 Z" fill="#fff"/>
    <path d="M150 0 C178 0 186 22 196 42 C208 64 226 68 258 68 H375" fill="none" stroke="#e9532b" stroke-width=".8"/>
  </svg>
  <div class="company-address"><b>VOLT3 Pty Ltd</b><br>9/40 Ironbark Way<br>Brookvale VIC 3180<br>ABN: 48 602 115 309<br>office@volt3.com.au</div>
  <div class="brand-divider"></div>
  <div class="brand-name">VOLT3</div>
  <div class="brand-mark"></div>
  <div class="date-tab" style="top:20px">11th July, 2025</div>
  <div class="title-bar" style="top:28px;width:156px">QUOTE</div>

  <div class="abs body-text" style="left:43px;top:53px"><b>TO,</b><br><b>Kestrel Interiors Pty Ltd</b><br>Dana Whitfield</div>
  <div class="doc-number" style="top:68px">Quote Number: 2252</div>
  <div class="abs body-text" style="left:43px;top:89px;width:280px">Thank you for allowing us to provide a quotation for your fire rating requirements. Works to be completed as per inspection at <b>14 Ashgrove Lane, Elmwood</b> as listed below.</div>

  <div class="section-bar" style="left:40px;top:106px;width:318px">Works Completed:</div>
  <div class="works-box" style="top:114px;height:201px"></div>
  <div class="works-divider" style="left:186px;top:114px;height:182px"></div>

  <div class="item" style="left:43px;top:118px"><h4>Level 5 – Electrical Cupboard</h4>1 x 700mm x 150mm penetration with cables &amp; wrap through slab floor</div>
  <div class="item" style="left:43px;top:148px"><h4>Level 4 – Electrical Cupboard</h4>1 x 700mm x 150mm penetration with cables &amp; wrap through slab floor</div>
  <div class="item" style="left:43px;top:178px"><h4>Level 3 – Electrical Cupboard</h4>1 x 700mm x 150mm penetration with cables &amp; wrap through slab floor</div>
  <div class="item" style="left:43px;top:208px"><h4>Level 2 – Electrical Cupboard</h4>1 x 700mm x 150mm penetration with cables (mortar pad) through slab floor</div>
  <div class="item" style="left:43px;top:238px"><h4>Level 1 – Electrical Cupboard</h4>1 x 700mm x 150mm penetration with cables (mortar pad) through slab floor</div>
  <div class="item" style="left:43px;top:268px"><h4>Level 1 – Comms Cupboard</h4>1 x 500mm x 150mm penetration with cables &amp; wrap through slab floor</div>

  <div class="item" style="left:192px;top:118px;width:142px"><h4>Ground Floor – Electrical Cupboard</h4>1 x 700mm x 150mm penetration empty through slab floor</div>
  <div class="item" style="left:192px;top:141px;width:142px"><h4>Ground Floor – Comms Cupboard</h4>1 x 500mm x 150mm penetration empty through slab floor</div>
  <div class="item" style="left:192px;top:164px;width:142px"><h4>Ground Floor – Switchroom</h4>2 x 600mm x 100mm penetration with cable tray &amp; wrap (ceiling to be cut)<br>through speed panel wall<br>1 x 200mm x 100mm penetration with cable tray &amp; wrap (ceiling to be cut)<br>through speed panel wall<br>1 x 700mm x 150mm penetration with cables &amp; wrap through slab floor<br>1 x 500mm x 150mm penetration with cables &amp; wrap through slab floor</div>
  <div class="item" style="left:192px;top:254px;width:142px"><h4>Basement 1 – Carpark</h4>1 x 700mm x 150mm penetration with cables &amp; wrap through slab floor<br>(smoke seal only)<br>1 x 500mm x 150mm penetration with cables through slab floor (smoke seal only)</div>

  <div class="abs" style="left:40px;top:296px;width:296px;height:.6px;background:var(--dark)"></div>
  <div class="abs" style="left:42px;top:302px;font-size:3.8px;line-height:7px;font-weight:300">*15 penetrations in total<br>*Includes penetration ID labels, fire certificate &amp; compliance fire penetration report</div>

  <div class="total-bar" style="top:320px;height:12px;line-height:12px">Price for Labour &amp; Materials - <b>TOTAL: &nbsp;$3,750 + GST</b></div>

  <div class="abs body-text" style="left:43px;top:335px;width:290px">Quoted price for installation and certification of the approved proprietary fire resistance tested products &amp; systems to AS1530 part 4 to maintain the required <b>FRL -/120/120</b> of the building element.</div>
  <div class="abs body-text strong" style="left:44px;top:352px">*Please note: Normal working hours 7am –3:30pm Monday to Friday</div>
  <div class="abs body-text" style="left:44px;top:365px;width:290px">Penalty rates apply for works after hours Clear access required at all times with priority. Contractor car parking to be provided</div>
  <div class="abs body-text" style="left:43px;top:380px">Valid 90 days &nbsp;&nbsp;<b>Terms: 30 days</b> &nbsp;&nbsp;No Retention<br>Purchase Order required before job start</div>

  <div class="notice-bar" style="top:398px">Fire Certification Certificate will only be provided upon full payment</div>
  <div class="accept-area">
    <div class="abs body-text" style="left:45px;top:3px;font-size:4.2px">To accept this quotation, please sign here and return</div>
    <div class="abs body-text" style="left:45px;top:18px;font-size:4.2px">Sign: <span class="sign-line" style="width:90px"></span></div>
    <div class="abs body-text" style="left:221px;top:18px;font-size:4.2px">Date: <span class="sign-line" style="width:69px"></span></div>
    <div class="abs body-text" style="left:45px;top:32px;font-size:4.2px">We look forward to proceeding upon your direction.</div>
    <div class="abs body-text" style="left:45px;top:46px;font-size:4.2px"><b>Kind Regards,</b></div>
    <div class="signature" role="img" aria-label="Handwritten signature" style="left:48px;top:53px;width:30px;height:13px"></div>
    <div class="abs body-text" style="left:45px;top:67px;font-size:4.2px">Owen Hartley</div>
  </div>
</section>

<section class="page page--cert" aria-label="Fire and smoke system certificate">
  <svg class="header-swoosh" width="375" height="72" viewBox="0 0 375 72">
    <path d="M140 0 C168 0 176 22 186 42 C198 64 220 68 252 68 H375 V0 Z" fill="#fff"/>
    <path d="M140 0 C168 0 176 22 186 42 C198 64 220 68 252 68 H375" fill="none" stroke="#e9532b" stroke-width=".8"/>
  </svg>
  <div class="company-address"><b>VOLT3 Pty Ltd</b><br>9/40 Ironbark Way<br>Brookvale VIC 3180<br>ABN: 48 602 115 309<br>office@volt3.com.au</div>
  <div class="brand-divider"></div>
  <div class="brand-name">VOLT3</div>
  <div class="brand-mark"></div>
  <div class="date-tab" style="top:51px">11th July, 2025</div>
  <div class="cert-title" style="top:60px">FIRE/SMOKE SYSTEM<br>CERTIFICATE</div>
  <div class="doc-number" style="top:79px;right:38px">Certificate Number: &nbsp;2262</div>

  <div class="abs body-text" style="left:43px;top:112px"><b>Client:</b> &nbsp;Certus Building Compliance<br><b>Job:</b> &nbsp;&nbsp;Parkview 12-18 Ridley Road, Fernhill – Building 4</div>
  <div class="abs body-text" style="left:43px;top:146px"><b>Reference:</b> &nbsp;Fire/smoke sealing of your various service penetrations as detailed below</div>
  <div class="abs body-text" style="left:43px;top:171px;width:280px"><b>VOLT3 Pty. Ltd.</b> certifies that as part of our contracted works, we have carried out the above fire protection at <b>Parkview 12-18 Ridley Road, Fernhill – Building 4</b> as instructed by <b>Priya Anand</b> of <b>Certus Building Compliance</b>.</div>
  <div class="abs body-text" style="left:43px;top:199px;width:280px">These works have been completed and checked using the approved proprietary fire resistance tested products &amp; systems <b>as per AS1530 part 4 &amp; AS4072 part 1</b></div>
  <div class="abs body-text" style="left:43px;top:221px">Any works that are modified, damaged or disturbed following completion are not covered by this certification.</div>
  <div class="abs body-text" style="left:43px;top:237px">Installed in accordance with the manufacturer's specifications.</div>

  <div class="abs body-text" style="left:43px;top:290px"><b>Signed:</b></div>
  <div class="signature" role="img" aria-label="Handwritten signature" style="left:43px;top:301px;width:40px;height:18px"></div>
  <div class="abs body-text" style="left:43px;top:323px"><b>Name:</b> &nbsp;Owen Hartley<br><b>Date:</b> &nbsp;30th January, 2026</div>

  <div class="section-bar" style="left:0;top:357px;width:296px;padding-left:43px">Works Completed:</div>
  <div class="abs body-text" style="left:42px;top:374px"><b>Ground Floor – Above Fire Doors Adjacent 51 Item 1</b><br>1 x 400mm x 400mm penetration with duct through plaster wall (one side only)</div>
  <div class="abs body-text" style="left:42px;top:398px"><b>Level 2 to Ground Floor – Hydraulic Riser (Lift Lobby) Item 2</b><br>2 x 100mm penetration with PVC pipe (caulk &amp; fixings) through slab roof</div>
  <div class="abs body-text" style="left:42px;top:421px"><b>Level 3 – Hydraulic Riser (Lift Lobby) Item 3</b><br>Further investigation required – excluded separate price to be provided if required.</div>
</section>

</body>
</html>
```